Mortgage Loan officer needs clean/modern business card design

Looking for a clean, modern 2-sided business card design. We like the earth tones used in our logo and website http://vukarhome-lending.example . Would also like to incorporate: 1) Something special to make our card stand out - a pop of color or embossed logo, for instance and 2) please include "Mortgage Loans" "Reverse Mortgages" "Private Money Loans" on back of card with the logo.

Front: Needs to include agent/company license info - see website. Agent name: Niall Hargrove

Here are fonts and colors used for our logo:
Font: Avenir Next
Colors:
#2c3539 - Dark Gray
#576870 - Light Gray
#ffffff - Background White

Target Market(s)

Prospects and current clients. Will also be distributing to people in professional network (attorneys and CPAs)

Industry/Entity Type

Business

Contact Information for Business Card

Include agent name, contact info, website on front, licensing info for agent an company. Logo and services offered on back

Font styles to use
Other font styles liked:
• Avenir Next

Requirements
Must have
• See project description
Should not have
• Nothing cheesy

```html
<!DOCTYPE html>
<html lang="en">
<head>
<meta charset="utf-8">
<title>Vukar Home Lending – Business Card</title>
<link href="https://fonts.googleapis.com/css2?family=Nunito+Sans:wght@400;600;700&display=swap" rel="stylesheet">
<style>
  :root {
    --dark-gray: #2c3539;
    --light-gray: #576870;
    --strip-gray: #3b474c;
    --accent-bar: #a9aeb1;
    --white: #ffffff;
    --page: #e9e7e4;
  }
  * { box-sizing: border-box; margin: 0; padding: 0; }
  html, body {
    width: 1200px; height: 1000px; overflow: hidden;
    background: var(--page);
    font-family: "Nunito Sans", "Avenir Next", sans-serif;
  }
  .card {
    position: absolute;
    box-shadow: 0 4px 14px rgba(0,0,0,.18);
    overflow: hidden;
  }

  /* Back of card */
  .card-back {
    left: 140px; top: 140px; width: 580px; height: 330px;
    background: var(--light-gray);
  }
  .card-back .top-band {
    position: absolute; left: 0; top: 0; right: 0; height: 140px;
    background: var(--dark-gray);
  }
  .card-back .brand-disc {
    position: absolute; left: 50%; top: 38px; width: 190px; height: 190px;
    margin-left: -95px; border-radius: 50%;
    background: var(--white);
    box-shadow: 3px 4px 0 rgba(0,0,0,.55);
    display: flex; align-items: center; justify-content: center;
    text-align: center;
  }
  .brand-name {
    color: var(--light-gray); font-weight: 400; line-height: 1.15;
  }
  .card-back .brand-name { font-size: 24px; }
  .services {
    position: absolute; left: 0; right: 0; bottom: 22px; height: 30px;
    background: var(--strip-gray);
    display: flex; align-items: center; justify-content: flex-end;
    padding-right: 14px;
  }
  .services li {
    list-style: none; color: var(--white); font-size: 15px;
    padding: 0 10px; letter-spacing: .2px;
    border-left: 3px solid var(--light-gray);
  }
  .services li:first-child { border-left: none; }

  /* Front of card */
  .card-front {
    left: 480px; top: 510px; width: 525px; height: 300px;
    background: var(--white);
  }
  .card-front .edge-bar {
    position: absolute; left: 6px; top: 48px; width: 14px; height: 175px;
    background: var(--accent-bar);
  }
  .card-front .brand-block {
    position: absolute; left: 32px; top: 48px; width: 200px; height: 175px;
    display: flex; align-items: center; justify-content: center; text-align: center;
  }
  .card-front .brand-name { font-size: 26px; }
  .agent-panel {
    position: absolute; left: 238px; top: 48px; width: 287px; height: 175px;
    background: var(--dark-gray); color: var(--white);
    padding: 16px 26px;
  }
  .agent-name { font-size: 21px; font-weight: 700; }
  .agent-name .surname { color: #9aa4a9; }
  .agent-title { font-size: 15px; margin-top: 6px; letter-spacing: .3px; }
  .agent-phone, .license { font-size: 11px; line-height: 1.3; }
  .license { margin-top: 14px; }
  .contact-row {
    position: absolute; left: 24px; right: 18px; top: 258px;
    display: flex; gap: 18px; font-size: 12.5px; color: var(--dark-gray);
    align-items: center;
  }
  .contact-row span { display: flex; align-items: center; gap: 5px; }
  .contact-row svg { width: 14px; height: 14px; }
</style>
</head>
<body>

<section class="card card-back">
  <div class="top-band"></div>
  <div class="brand-disc">
    <div class="brand-name">Vukar Home<br>Lending</div>
  </div>
  <ul class="services">
    <li>MORTGAGE LOANS</li>
    <li>REVERSE MORTGAGES</li>
    <li>PRIVATE MONEY LOANS</li>
  </ul>
</section>

<section class="card card-front">
  <div class="edge-bar"></div>
  <div class="brand-block">
    <div class="brand-name">Vukar Home<br>Lending</div>
  </div>
  <div class="agent-panel">
    <div class="agent-name">Niall <span class="surname">Hargrove</span></div>
    <div class="agent-title">LOAN OFFICER</div>
    <div class="agent-phone">+ 650 - 555 - 0147</div>
    <div class="license">
      Fed and State License<br>
      NMLS:100245<br>
      DRE:02004417<br>
      CO: DRE:02008830/NMLS:100890
    </div>
  </div>
  <div class="contact-row">
    <span>
      <svg viewBox="0 0 14 14" aria-hidden="true"><circle cx="7" cy="7" r="7" fill="#2c3539"/><path d="M4 5.2c0-.8.6-1.2 1.2-1.2h3.6c.6 0 1.2.4 1.2 1.2v.6H8.6v-.5H5.4v.5H4zM4.2 6.4h5.6L10 10H4z" fill="#fff"/></svg>
      + 408-555-0120 x 214
    </span>
    <span>
      <svg viewBox="0 0 14 14" aria-hidden="true"><circle cx="7" cy="7" r="7" fill="#2c3539"/><rect x="4.5" y="3.3" width="5" height="2.4" fill="#fff"/><rect x="3.5" y="6.2" width="7" height="3" rx=".5" fill="#fff"/><rect x="4.5" y="8.4" width="5" height="2.4" fill="#fff"/></svg>
      + 408 - 555 - 0193
    </span>
    <span>
      <svg viewBox="0 0 14 14" aria-hidden="true"><circle cx="7" cy="7" r="7" fill="#2c3539"/><g fill="none" stroke="#fff" stroke-width=".9"><circle cx="7" cy="7" r="3.8"/><ellipse cx="7" cy="7" rx="1.6" ry="3.8"/><path d="M3.2 7h7.6"/></g></svg>
      www.vukarhome-lending.example
    </span>
  </div>
</section>

</body>
</html>
```